Hip Surgeon needs a web page re-design.

I have a web page to provide information about the diseases of the hip joint for the patients from my private practice since 2008. I need a re-design job for a fresh new look.
We have made a new logo and a new stationery design here in Marqueloft (please see the uploaded files) and I want to make my web page look-alike the new design concepts.
I like the color blue and tones of blue, matching my logo and stationery.
I don't like "busy" designs. It must be clean, elegant and ease to read. The final design should be "mobile friendly" if possible.
Please visit my website www.vilacorendasul.com.br to take a look and get some inspiration.

```html
<!DOCTYPE html>
<html lang="pt-BR">
<head>
<meta charset="utf-8">
<title>Dr. Rafael M. Tavares — Cirurgia do Quadril</title>
<link href="https://fonts.googleapis.com/css2?family=Open+Sans:wght@400;600;700&display=swap" rel="stylesheet">
<style>
:root{
  --blue:#1b8fd6;
  --blue-dark:#0f6fb3;
  --navy:#0d3f73;
  --navy-deep:#0a2f57;
  --gray-bg:#efefef;
  --text:#555;
  --muted:#888;
  --white:#fff;
}
*{margin:0;padding:0;box-sizing:border-box}
html,body{width:800px;height:1200px;overflow:hidden}
body{font-family:"Open Sans",Arial,sans-serif;color:var(--text);background:var(--white)}
.page{width:800px;height:1200px;position:relative}

.topbar{height:26px;border-bottom:1px solid #e4e4e4;display:flex;align-items:center;justify-content:space-between;padding:0 90px;font-size:8px;color:var(--muted);white-space:nowrap}
.topbar .right{display:flex;align-items:center;gap:6px}
.social-dot{width:12px;height:12px;border-radius:2px;background:#bbb}
.search{width:90px;height:14px;border:1px solid #ccc;margin-left:10px}

.header{height:80px;display:flex;align-items:center;justify-content:space-between;padding:0 90px}
.brand{display:flex;align-items:center;gap:8px;white-space:nowrap}
.brand-mark{width:30px;height:30px;border-radius:50%;background:var(--blue)}
.brand-name{font-size:16px;font-weight:600;color:var(--blue);line-height:1.15}
.brand-sub{font-size:10px;color:var(--blue)}
.nav{display:flex;height:80px}
.nav a{display:flex;align-items:center;padding:0 11px;font-size:8px;font-weight:600;color:#666;text-decoration:none;white-space:nowrap}
.nav a.active{background:var(--blue);color:var(--white);padding:0 14px}

.hero{height:320px;position:relative;background:linear-gradient(90deg,#1680c7 0%,#1e92d8 55%,#3aa6e3 100%);overflow:hidden}
.hero-visual{position:absolute;right:90px;top:0;width:360px;height:320px;background:radial-gradient(ellipse at center,#9fd3f5 0%,#4fafe6 45%,rgba(30,146,216,0) 75%)}
.hero-copy{position:absolute;left:90px;top:110px;width:300px;color:var(--white)}
.hero-copy h1{font-size:28px;font-weight:400;margin-bottom:10px}
.hero-copy p{font-size:8.5px;line-height:1.5;margin-bottom:12px}
.btn{display:inline-block;background:var(--blue-dark);color:var(--white);font-size:7px;font-weight:700;padding:5px 12px;border-radius:2px}
.hero .btn{background:#0d5e9e}
.arrow{position:absolute;top:145px;width:22px;height:22px;border-radius:50%;background:rgba(255,255,255,.85);display:flex;align-items:center;justify-content:center}
.arrow.left{left:10px}.arrow.right{right:10px}
.dots{position:absolute;bottom:12px;left:90px;display:flex;gap:6px}
.dots span{width:5px;height:5px;border-radius:50%;background:rgba(255,255,255,.5)}
.dots span:first-child{background:var(--white)}

.intro{height:260px;position:relative}
.intro-band{position:absolute;left:0;right:0;top:60px;height:182px;background:var(--gray-bg)}
.intro-photo{position:absolute;left:112px;top:41px;width:168px;height:219px;background:linear-gradient(180deg,#c9d3dc,#e9edf0)}
.intro-copy{position:absolute;left:330px;top:78px;width:380px}
.intro-copy h2{font-size:15px;font-weight:700;color:var(--blue)}
.intro-copy h3{font-size:13px;font-weight:400;color:#444;margin:2px 0 14px}
.intro-copy p{font-size:8px;line-height:1.6;margin-bottom:12px}

.features{height:296px;display:flex;justify-content:space-between;padding:90px 90px 0}
.feature{width:180px;text-align:center}
.feature-icon{height:44px;display:flex;align-items:center;justify-content:center;margin-bottom:8px}
.feature-icon .plain{width:32px;height:32px;background:#444;border-radius:4px}
.feature h4{font-size:11px;font-weight:600;color:var(--blue);margin-bottom:10px}
.feature p{font-size:8px;line-height:1.6;margin-bottom:14px}
.more{font-size:7.5px;color:#666}

.footer{height:190px;background:var(--navy);display:flex;justify-content:space-between;padding:18px 90px 0;color:#cfe0f0;font-size:7px;line-height:1.5}
.footer h5{font-size:8px;color:var(--white);margin-bottom:8px;font-weight:700}
.fcol{width:190px}
.fcol .item{border-bottom:1px solid #28598b;padding:6px 0}
.fcol b{color:var(--white)}
.fcol .gap{margin-top:8px}
.subscribe{display:flex;margin:8px 0 16px}
.subscribe .field{flex:1;height:14px;background:var(--white)}
.subscribe .go{background:var(--blue);color:var(--white);font-size:6.5px;padding:0 8px;display:flex;align-items:center}
.fsocial{display:flex;gap:4px;margin-top:4px}
.fsocial span{width:11px;height:11px;border-radius:50%;background:#5a86b3}
.fbtn{display:inline-block;background:var(--blue);color:var(--white);padding:3px 12px;margin-top:10px;font-size:6.5px;font-weight:700}

.bottombar{height:28px;background:var(--navy-deep);display:flex;align-items:center;justify-content:space-between;padding:0 90px;font-size:7px;color:#aac3db}
.bottombar nav{display:flex;gap:22px}
</style>
</head>
<body>
<div class="page">
  <div class="topbar">
    <span>contato@clinicaquadrilsul.com.br &nbsp;&nbsp; +55 (41) 3000-0417</span>
    <div class="right">
      <span class="social-dot"></span><span class="social-dot"></span><span class="social-dot"></span><span class="social-dot"></span>
      <span class="search"></span>
    </div>
  </div>

  <header class="header">
    <div class="brand">
      <span class="brand-mark"></span>
      <div><div class="brand-name">Dr. Rafael M. Tavares</div><div class="brand-sub">Cirurgia do Quadril</div></div>
    </div>
    <nav class="nav">
      <a class="active">HOME</a><a>SOBRE MIM</a><a>ATUALIZAÇÕES</a><a>LINKS</a><a>DOWNLOAD</a><a>CONTATO</a>
    </nav>
  </header>

  <section class="hero">
    <div class="hero-visual" role="img" aria-label="Radiografia de quadril com prótese"></div>
    <div class="hero-copy">
      <h1>Próteses de quadril</h1>
      <p>Saiba como funciona a cirurgia de prótese de quadril, quando ela é indicada e como é a recuperação do paciente após o procedimento.</p>
      <span class="btn">CONTINUE LENDO</span>
    </div>
    <div class="arrow left"><svg width="8" height="10"><path d="M6 1 2 5l4 4" stroke="#1b8fd6" stroke-width="2" fill="none"/></svg></div>
    <div class="arrow right"><svg width="8" height="10"><path d="M2 1l4 4-4 4" stroke="#1b8fd6" stroke-width="2" fill="none"/></svg></div>
    <div class="dots"><span></span><span></span><span></span><span></span><span></span></div>
  </section>

  <section class="intro">
    <div class="intro-band"></div>
    <div class="intro-photo" role="img" aria-label="Retrato do médico de jaleco branco"></div>
    <div class="intro-copy">
      <h2>DR. RAFAEL MOREIRA TAVARES</h2>
      <h3>Seja bem vindo ao site “Saúde do Quadril”!</h3>
      <p>O objetivo deste site é fornecer aos pacientes informações claras sobre as principais doenças da articulação do quadril, seus tratamentos e os cuidados antes e depois da cirurgia.</p>
      <span class="btn">SAIBA MAIS</span>
    </div>
  </section>

  <section class="features">
    <div class="feature">
      <div class="feature-icon"><span class="plain"></span></div>
      <h4>VEJA NOSSO CANAL</h4>
      <p>Assista aos vídeos explicativos sobre as doenças do quadril, exames, cirurgias e reabilitação.</p>
      <span class="more">Continue lendo ›</span>
    </div>
    <div class="feature">
      <div class="feature-icon"><svg width="36" height="36" viewBox="0 0 40 40" fill="none" stroke="#444" stroke-width="2.5"><path d="M20 4v22M12 18l8 8 8-8M5 26v9h30v-9"/></svg></div>
      <h4>DOWNLOAD DE MANUAL</h4>
      <p>PRÓTESE DE QUADRIL: cuidados após a cirurgia.</p>
      <span class="more">Continue lendo ›</span>
    </div>
    <div class="feature">
      <div class="feature-icon"><svg width="36" height="36" viewBox="0 0 40 40" fill="none" stroke="#1b8fd6" stroke-width="2.5"><path d="M7 24v-5a13 13 0 0 1 26 0v5"/><rect x="5" y="23" width="7" height="11" rx="2"/><rect x="28" y="23" width="7" height="11" rx="2"/></svg></div>
      <h4>AGENDA SUA CONSULTA</h4>
      <p>Marque seu horário pelo telefone ou pelo formulário de contato e tire suas dúvidas.</p>
      <span class="more">Continue lendo ›</span>
    </div>
  </section>

  <footer class="footer">
    <div class="fcol">
      <h5>ÚLTIMAS ATUALIZAÇÕES</h5>
      <div class="item">Novo manual de cuidados após a cirurgia de prótese</div>
      <div class="item">Novo vídeo sobre artrose do quadril no canal</div>
      <div class="item">Atualização sobre dor no quadril em atletas</div>
    </div>
    <div class="fcol">
      <h5>CONTATOS</h5>
      <b>TELEFONE</b><br>+55 (41) 3000-0417<br>
      <div class="gap"><b>CONSULTÓRIO</b><br>Rua das Acácias, 120 — Sala 8<br>Curitiba — PR</div>
      <span class="fbtn">VER NO MAPA</span>
    </div>
    <div class="fcol">
      <h5>SUBSCRIBE NEWSLETTER</h5>
      Receba as novidades do site por e-mail.
      <div class="subscribe"><span class="field"></span><span class="go">ASSINAR</span></div>
      <h5>SOCIAL NETWORKS</h5>
      <div class="fsocial"><span></span><span></span><span></span><span></span></div>
    </div>
  </footer>
  <div class="bottombar">
    <span>Copyright 2015 Dr. Rafael M. Tavares</span>
    <nav><span>HOME</span><span>SOBRE MIM</span><span>ATUALIZAÇÕES</span><span>LINKS</span><span>DOWNLOAD</span><span>CONTATO</span></nav>
  </div>
</div>
</body>
</html>
```